Flyer for a mint vending business (KDM). Draft included... need creative mind to complete!

This flyer will be for a mint vending machine business. I am the owner and the flyer will be given to business owners who will be placing the machines in their business for information on the placement. The flyer will be 6" x 9" so the verbiage needs to fit within the size and be readable. I have included a draft of the basic design (both front and back). I would like it to be colorful and eye-catching but professional. I have included the main image of the mint machine (for the front page) in the uploaded files. The KDM logo mentioned on page two is from the business card (also uploaded). The mint image (page one) can be a stock image- would like it to be round, in a silver wrapper and say "Mint" on the front. The information blurbs on the front surrounding the image should have some form of starburst around the text (as shown in the copy with handwritten notes). Creativity input on font, color and background from the designer is appreciated.

```html
<!DOCTYPE html>
<html lang="en">
<head>
<meta charset="utf-8">
<title>Mint Machines Flyer</title>
<link href="https://fonts.googleapis.com/css2?family=Oswald:wght@500;600;700&family=Montserrat:wght@400;500;600;700;800&display=swap" rel="stylesheet">
<style>
  :root {
    --navy: #0f2147;
    --yellow: #fdb913;
    --yellow-deep: #f7a600;
    --green-light: #9fe08a;
    --green: #2fb07a;
    --teal: #14977f;
    --white: #ffffff;
    --ink: #1f2a44;
    --muted: #3a4560;
  }
  * { margin: 0; padding: 0; box-sizing: border-box; }
  html, body { width: 847px; height: 1200px; overflow: hidden; background: var(--white); }
  .flyer {
    position: relative; width: 847px; height: 1200px; overflow: hidden;
    background: var(--white); font-family: "Montserrat", Arial, sans-serif; color: var(--ink);
  }
  .abs { position: absolute; }
  .backdrop { left: 0; top: 0; }

  .hero-title { left: 56px; top: 104px; color: var(--white); font-family: "Oswald", Impact, sans-serif; }
  .hero-title .big { font-size: 104px; font-weight: 700; line-height: 1; letter-spacing: 1px; }
  .hero-title .line { font-family: "Montserrat", Arial, sans-serif; font-weight: 800; text-transform: uppercase; line-height: 1.05; }
  .hero-title .yellow { color: var(--yellow); font-size: 34px; }
  .hero-title .white { font-size: 21px; font-weight: 600; }

  .support-callout {
    left: 48px; top: 392px; width: 218px; height: 196px; background: var(--yellow);
    border-radius: 14px; text-align: center; color: var(--navy); padding: 16px 8px 0;
  }
  .support-callout::after {
    content: ""; position: absolute; left: 50%; bottom: -20px; transform: translateX(-50%);
    border-left: 18px solid transparent; border-right: 18px solid transparent; border-top: 20px solid var(--yellow);
  }
  .support-callout .kicker { font-weight: 800; font-size: 16px; line-height: 1.1; white-space: nowrap; }
  .support-callout .headline { font-family: "Oswald", Impact, sans-serif; font-weight: 700; font-size: 42px; line-height: 1.1; }
  .support-callout .note { font-size: 14px; font-weight: 500; line-height: 1.25; }
  .support-callout .foot { font-family: "Oswald", Impact, sans-serif; font-weight: 700; font-size: 30px; line-height: 1.2; margin-top: 2px; }

  .free-badge {
    left: 594px; top: 396px; width: 210px; height: 210px; border-radius: 50%;
    background: var(--navy); border: 10px solid var(--yellow); color: var(--white);
    display: flex; flex-direction: column; align-items: center; justify-content: center; text-align: center;
  }
  .free-badge .free { font-family: "Oswald", Impact, sans-serif; font-size: 58px; font-weight: 600; line-height: 0.95; }
  .free-badge .placement { font-weight: 800; font-size: 17px; letter-spacing: 0.5px; }
  .free-badge .small { font-size: 10px; font-weight: 600; line-height: 1.2; text-transform: uppercase; margin-top: 2px; }
  .free-badge .ever { font-family: "Oswald", Impact, sans-serif; font-size: 34px; font-weight: 600; letter-spacing: 6px; line-height: 1.1; }

  .section-title { font-weight: 800; font-size: 22px; text-transform: uppercase; }
  .section-title .accent { color: var(--yellow-deep); }
  .section-title .dark { color: var(--navy); }
  .body-copy { font-size: 11.5px; line-height: 1.55; color: var(--muted); }

  .maintenance { left: 60px; top: 660px; width: 330px; }
  .maintenance .body-copy { margin-top: 10px; }
  .treat { left: 412px; top: 662px; width: 380px; }
  .treat .section-title { margin-top: 8px; }

  .tagline {
    left: 60px; top: 806px; width: 740px; color: var(--navy); font-size: 16px; font-weight: 500;
    text-transform: uppercase; line-height: 1.35;
  }

  .perks {
    left: 50px; top: 880px; width: 748px; height: 178px; background: var(--yellow);
    border-radius: 18px; display: flex;
  }
  .perk { flex: 1; text-align: center; color: var(--navy); padding-top: 44px; }
  .perk + .perk { border-left: 3px dotted var(--white); margin: 14px 0; padding-top: 36px; }
  .perk-title { font-weight: 800; font-size: 18px; text-transform: uppercase; }
  .perk-text { font-size: 14px; font-weight: 500; line-height: 1.3; margin-top: 4px; }
  .perk-icon {
    position: absolute; width: 64px; height: 64px; border-radius: 50%; background: var(--navy);
    display: flex; align-items: center; justify-content: center;
  }

  .closing {
    left: 0; top: 1118px; width: 847px; text-align: center; color: var(--white);
    font-size: 18px; font-weight: 500; line-height: 1.35;
  }
</style>
</head>
<body>
<main class="flyer">
  <svg class="abs backdrop" width="847" height="1200" viewBox="0 0 847 1200">
    <defs>
      <linearGradient id="storeTone" x1="0" y1="0" x2="1" y2="1">
        <stop offset="0" stop-color="#cfe9dc"/>
        <stop offset="0.5" stop-color="#7fbf9b"/>
        <stop offset="1" stop-color="#dfe6e2"/>
      </linearGradient>
      <radialGradient id="mintCircle" cx="0.3" cy="0.25" r="0.8">
        <stop offset="0" stop-color="#9fe08a"/>
        <stop offset="0.55" stop-color="#2fb07a"/>
        <stop offset="1" stop-color="#14977f"/>
      </radialGradient>
      <linearGradient id="machineTone" x1="0" y1="0" x2="0" y2="1">
        <stop offset="0" stop-color="#e8eef0"/>
        <stop offset="0.45" stop-color="#d6332b"/>
        <stop offset="0.6" stop-color="#2a2a2a"/>
        <stop offset="1" stop-color="#111"/>
      </linearGradient>
      <linearGradient id="leafTone" x1="0" y1="0" x2="1" y2="1">
        <stop offset="0" stop-color="#8fe07a"/>
        <stop offset="1" stop-color="#2f9a3f"/>
      </linearGradient>
    </defs>
    <rect role="img" aria-label="Blurred supermarket aisle with shelves" x="0" y="0" width="847" height="620" fill="url(#storeTone)"/>
    <path d="M0 560 Q300 640 847 590 L847 660 L0 660 Z" fill="var(--white)"/>
    <circle cx="150" cy="110" r="450" fill="url(#mintCircle)"/>
    <path d="M0 580 Q250 470 470 240" fill="none" stroke="var(--white)" stroke-width="3" stroke-dasharray="2 8" stroke-linecap="round"/>
    <ellipse role="img" aria-label="Fresh mint leaves" cx="160" cy="62" rx="70" ry="48" fill="url(#leafTone)"/>
    <rect role="img" aria-label="Mint vending machine on a black stand" x="540" y="72" width="150" height="520" rx="40" fill="url(#machineTone)"/>
    <path d="M0 1030 Q420 940 847 955 L847 1200 L0 1200 Z" fill="var(--yellow)"/>
    <path d="M0 1060 Q430 990 847 1010 L847 1200 L0 1200 Z" fill="var(--navy)"/>
    <path d="M600 1000 Q760 985 847 930" fill="none" stroke="var(--yellow)" stroke-width="3" stroke-dasharray="2 8" stroke-linecap="round"/>
  </svg>

  <header class="abs hero-title">
    <div class="big">MINT</div>
    <div class="line yellow">Machines</div>
    <div class="line white">The highlights in a</div>
    <div class="line yellow">Mint wrappers!</div>
  </header>

  <aside class="abs support-callout">
    <div class="kicker">YOUR SUPPORT HELPS</div>
    <div class="headline">VATERANS!</div>
    <div class="note">A donation is placed directly from the machine in your store!</div>
    <div class="foot">EVERY MONTH</div>
  </aside>

  <div class="abs free-badge">
    <div class="free">FREE</div>
    <div class="placement">PLACEMENT</div>
    <div class="small">No charge to the<br>business owners</div>
    <div class="ever">EVER</div>
  </div>

  <section class="abs maintenance">
    <h2 class="section-title"><span class="accent">Maintenance</span> <span class="dark">on us!</span></h2>
    <p class="body-copy">Yes, web actually service our machines on a regular basis. Machines will be stocked cleaned and are of high quality, so no breakdowns.</p>
  </section>

  <section class="abs treat">
    <p class="body-copy">A benefit for your customer or employee! Our own chocolate mint is a delicious, top-of-the-line product and the perfect quick.</p>
    <h2 class="section-title"><span class="accent">Refreshing</span> <span class="dark">treat</span></h2>
  </section>

  <p class="abs tagline">Sharp looking classy machines that take up little space. Can be placed on a stand or countertop you decide!</p>

  <section class="abs perks">
    <div class="perk">
      <div class="perk-title">No contract</div>
      <div class="perk-text">Unless preferred, in which case, we<br>have one ready to go.</div>
    </div>
    <div class="perk">
      <div class="perk-title">No liability</div>
      <div class="perk-text">No worries, Zero liability for the business<br>owner our machines are insured.</div>
    </div>
  </section>

  <div class="abs perk-icon" style="left:186px; top:850px;">
    <svg width="34" height="34" viewBox="0 0 24 24" fill="var(--white)" aria-hidden="true">
      <path d="M21 16v-2l-8-5V3.5a1.5 1.5 0 0 0-3 0V9l-8 5v2l8-2.5V19l-2 1.5V22l3.5-1 3.5 1v-1.5L13 19v-5.5z"/>
    </svg>
  </div>
  <div class="abs perk-icon" style="left:573px; top:850px;">
    <svg width="32" height="32" viewBox="0 0 24 24" fill="var(--white)" aria-hidden="true">
      <path d="M9 4 7.5 6H4a2 2 0 0 0-2 2v10a2 2 0 0 0 2 2h16a2 2 0 0 0 2-2V8a2 2 0 0 0-2-2h-3.5L15 4z"/>
      <circle cx="12" cy="13" r="4" fill="var(--navy)"/>
      <circle cx="12" cy="13" r="2.5" fill="var(--white)"/>
    </svg>
  </div>

  <footer class="abs closing">Work with a local, family owned business. if there are needs or<br>concerns, you will speak with us... directly</footer>
</main>
</body>
</html>
```